Saltbush Healing needs business card design

I need a business card design for a new energy healing business in Perth Australia. As an energy healer I am quite earthy and practical rather than floaty and fairydust.
One of the techniques I use is unique in Australia but used internationally (US, UK and Europe). I practice with Coastal Pathway Therapy, Reiki and massage as well as some other techniques I developed personally. I am starting to incorporate sound healing into my practice. I literally change people's lives. The potential for each client is wide open. A key skill I bring to my practice is the capacity for making difficult situations seem more fun and less stressful.
Clients are likely to be depressed, physically unwell, going through a difficult time, unhappy with their current situation. They are people looking for new options to solve a difficult existing problem. They have probably tried other avenues before they come to me. They are open to something different.

I would like to communicate that the client and I work together for their healing and personal growth. I would like to convey that while the work of changing is challenging it can also be fun.

Hi all, info required on the card is:

Name
Title: Healer
contact number (mobile)
I don''t have a logo - I would be interested in seeing designs that use the whole card as well as the traditional logo on one side / in one corner. Whatever ''look/feel'' I choose will carry over to the website as well.

thanks
Meg

Reason: One or two of the designs caught my eye and many appeal for different reasons, but nothing is quite right for me. I've invited a couple of other designers to contribute so I wanted to give them time to be involved. kind regards Meg

Thank you all for the fabulous designs. I really appreciated the thought that many people put into my brief and a number of designs captured important things about what I was trying to say. It was a hard choice between 3 designs in the end.
thanks again and kind regards
Meg

Target Market(s)

people looking for new options to solve a difficult existing problem

Industry/Entity Type

Massage

Logo styles of interest
Abstract Logo
Requirements
Must have
• include green and blue
Nice to have
• hands, tea / teapots , the ocean, stepping stones

```html
<!DOCTYPE html>
<html lang="en">
<head>
<meta charset="utf-8">
<title>Saltbush Healing – Business Card</title>
<link rel="stylesheet" href="https://fonts.googleapis.com/css2?family=Tinos:ital,wght@0,400;0,700;1,400&display=swap">
<style>
  :root {
    --band-top: #8fd8f7;
    --band-bottom: #bde9fb;
    --ink: #111111;
    --rule-green: #3a9a3a;
    --brand-blue: #2a7fc0;
    --brand-green: #3aa655;
    --card-edge: #9a9a9a;
    --paper: #ffffff;
  }
  * { margin: 0; padding: 0; box-sizing: border-box; }
  html, body {
    width: 1200px; height: 777px; overflow: hidden;
    background: var(--paper);
  }
  .card {
    position: relative;
    width: 1200px; height: 777px;
    background: var(--paper);
    border: 2px solid var(--card-edge);
    font-family: "Tinos", "Times New Roman", serif;
    color: var(--ink);
  }
  .side-band {
    position: absolute; left: 0; top: 0;
    width: 155px; height: 100%;
    background: linear-gradient(180deg, var(--band-top), var(--band-bottom));
  }
  .side-band__text {
    position: absolute;
    left: 78px; top: 388px;
    transform: translate(-50%, -50%) rotate(-90deg);
    white-space: nowrap;
    text-align: center;
    font-style: italic;
    font-size: 30px;
    line-height: 38px;
  }
  .brand {
    position: absolute;
    left: 710px; top: 244px;
    width: 460px;
    display: flex; align-items: center; justify-content: center; gap: 14px;
  }
  .brand__dot {
    width: 30px; height: 30px; border-radius: 50%;
    background: var(--brand-green);
    flex: none;
  }
  .brand__name {
    font-size: 40px;
    line-height: 48px;
    font-weight: 700;
    color: var(--brand-blue);
    white-space: nowrap;
  }
  .holder-name {
    position: absolute;
    left: 194px; top: 252px;
    font-style: italic;
    font-weight: 400;
    font-size: 46px;
  }
  .rule {
    position: absolute;
    left: 191px; top: 318px;
    width: 980px; height: 2px;
    background: var(--rule-green);
  }
  .contact {
    position: absolute;
    left: 196px; top: 366px;
    font-style: italic;
    font-size: 26px;
    line-height: 44px;
    list-style: none;
  }
  .contact__gap { height: 44px; }
  .tagline {
    position: absolute;
    left: 700px; top: 358px;
    width: 470px;
    text-align: center;
    font-size: 58px;
    line-height: 82px;
  }
  .website {
    position: absolute;
    left: 700px; top: 588px;
    width: 470px;
    text-align: center;
    font-style: italic;
    font-size: 26px;
  }
</style>
</head>
<body>
  <main class="card">
    <aside class="side-band">
      <p class="side-band__text">Coastal Pathway Therapy<br>Reiki and Massage</p>
    </aside>

    <div class="brand">
      <span class="brand__dot"></span>
      <span class="brand__name">Saltbush Healing</span>
    </div>

    <h1 class="holder-name">Your Name</h1>
    <div class="rule"></div>

    <ul class="contact">
      <li>17 Banksia Lane</li>
      <li>Your Address Line 2</li>
      <li class="contact__gap"></li>
      <li>Phone</li>
      <li>Fax</li>
      <li>E-mail: care@saltbushhealing.com.au</li>
    </ul>

    <p class="tagline">Change your<br>Life today!</p>
    <p class="website">www.saltbushhealing.com.au</p>
  </main>
</body>
</html>
```